New design for PeopleDeskly

We are at the start of the process of evolving an existing business, and have just developed a new logo that will guide the look and feel of the rest of the site.

PeopleDeskly.com.au will be the place to go for small business owners that need guidance and tools on how to look after HR functions such as recruitment and performance management amongst other aspects.

The existing site that is going to be evolved in www.staffingpathguide.com.au - while some of the content will remain, the entire look of the site needs to change, and a new homepage and other pages need to be developed.

For this project, we'd like the new homepage to be designed to lead the way for how the rest of the pages will look moving forward.

We're looking for a clean, clear and modern design. It should not feel cluttered or busy

The wireframe for the new homepage, and another landing page are attached.

Target Market(s)

Small and medium business owners - slightly male skew

Industry/Entity Type

Small Business

Requirements
Must have
• - Should be clean and simple
- The overall feel from the new logo (attached to the project) should be integrated into all elements of the site
- Should communicate that the site is easy to navigate
- Should communicate that the site is friendly and approachable
- Should communicate that the site is professional (for small businesses)
Nice to have
• This homepage for this site is quite a good design reference in terms of clean design.

http://www.chorebadger.example/

For PeopleDeskly though, the 3 boxes under the main image should appear above the fold though.

Also, happy for one other colour to be introduced to highlight call to action buttons etc.
Should not have
• Must not be cluttered
Should not introduce more than one additional colour to the existing colours from the logo

```html
<!DOCTYPE html>
<html lang="en">
<head>
<meta charset="utf-8">
<title>PeopleDeskly – HR guidance for small business</title>
<link rel="stylesheet" href="https://fonts.googleapis.com/css2?family=Roboto+Condensed:wght@400;700&family=Source+Sans+3:wght@400;600&display=swap">
<style>
  :root {
    --brand-blue: #0b6bbf;
    --ink: #3a3a3a;
    --line: #c9d3dc;
    --white: #ffffff;
    --icon: #6e6e6e;
  }
  * { box-sizing: border-box; margin: 0; padding: 0; }
  html, body { width: 1200px; height: 984px; overflow: hidden; }
  body {
    position: relative;
    background: linear-gradient(#f8fbfd 0, #eef3f8 100px, #f6f9fc 101px, #edf3f9 870px);
    font-family: "Source Sans 3", "Myriad Pro", sans-serif;
    color: var(--ink);
  }
  .site-header {
    position: absolute; left: 0; top: 0; width: 1200px; height: 101px;
    background: linear-gradient(#ffffff, #eef4fa);
    border-bottom: 1px solid #bcd6ee;
  }
  .brand {
    position: absolute; left: 184px; top: 30px;
    display: flex; align-items: center; gap: 8px;
    font-family: "Roboto Condensed", sans-serif; font-weight: 700;
    font-size: 30px; color: var(--brand-blue); letter-spacing: -0.5px;
  }
  .brand-dot { width: 26px; height: 26px; border-radius: 50%; background: var(--brand-blue); }
  .utility-links { position: absolute; left: 886px; top: 16px; display: flex; gap: 28px; }
  .utility-links svg { width: 30px; height: 30px; fill: var(--icon); }

  .main-nav {
    position: absolute; left: 145px; top: 106px; width: 910px; height: 35px;
    border: 1px solid var(--line); border-radius: 5px;
    background: linear-gradient(#ffffff, #f1f4f7);
    font-family: "Roboto Condensed", sans-serif; font-size: 16.5px; color: #4a4a4a;
  }
  .main-nav a {
    position: absolute; top: 0; height: 33px; line-height: 33px;
    color: inherit; text-decoration: none; white-space: nowrap;
  }
  .main-nav a.is-active { background: var(--brand-blue); color: var(--white); padding: 0 11px; }

  .hero {
    position: absolute; left: 145px; top: 145px; width: 910px; height: 340px;
    border-radius: 6px; overflow: hidden; border: 1px solid var(--line);
    box-shadow: 0 8px 10px -6px rgba(0,0,0,.35);
  }
  .hero-photo {
    position: absolute; inset: 0;
    background: linear-gradient(90deg, #eef2f4 0%, #e4e9ec 40%, #d9d2c8 65%, #b89b85 80%, #3a4150 100%);
  }
  .hero-tab { position: absolute; left: 0; top: 0; width: 48px; height: 100%; background: var(--brand-blue); }
  .hero-label {
    position: absolute; left: 0; top: 12px; height: 34px; width: 62px;
    background: var(--brand-blue); border-radius: 0 17px 17px 0;
    color: var(--white); font-family: "Roboto Condensed", sans-serif; font-weight: 700;
    font-size: 21px; line-height: 34px; padding-left: 12px;
  }
  .hero-label::after {
    content: ""; position: absolute; right: 8px; top: 12px;
    border-left: 8px solid #fff; border-top: 5px solid transparent; border-bottom: 5px solid transparent;
  }
  .hero-dots { position: absolute; right: 16px; bottom: 24px; display: flex; gap: 4px; }
  .hero-dots span { width: 11px; height: 11px; background: #fff; }
  .hero-dots span.is-current { background: var(--brand-blue); }

  .column { position: absolute; top: 510px; }
  .column h2 {
    font-family: "Roboto Condensed", sans-serif; font-weight: 400;
    font-size: 23px; line-height: 28px; color: var(--brand-blue); text-align: center; margin-bottom: 14px;
  }
  .column p { font-size: 13px; line-height: 22px; color: var(--ink); }
  .column-divider { position: absolute; top: 500px; width: 1px; height: 355px; background: linear-gradient(transparent, #d8e4ef 20%, #d8e4ef 80%, transparent); }

  .about { left: 168px; width: 258px; }
  .about h2 { margin-top: 2px; }
  .about p { text-align: justify; margin-bottom: 22px; }

  .news { left: 465px; width: 270px; }
  .news-item { display: flex; gap: 12px; height: 84px; }
  .date-badge {
    flex: none; width: 53px; height: 52px; border: 1px solid var(--line); border-radius: 6px;
    background: linear-gradient(#fff, #f0f3f6); text-align: center; color: #555; font-size: 10px; line-height: 11px; padding-top: 3px;
  }
  .date-badge strong { display: block; font-weight: 400; font-size: 24px; line-height: 26px; color: #444; }

  .partners { left: 773px; width: 258px; height: 360px; }
  .partner { position: absolute; left: 0; width: 258px; height: 90px; }
  .partner-badge {
    position: absolute; left: 0; top: 0; width: 101px; height: 75px; background: #fff; border: 1px solid #dde3e8;
    box-shadow: 0 1px 3px rgba(0,0,0,.15); display: flex; align-items: center; justify-content: center;
  }
  .partner-badge span { width: 40px; height: 40px; border-radius: 50%; background: #d7e4f0; }
  .partner p { position: absolute; left: 114px; top: 0; width: 144px; text-align: justify; }
  .partner cite { position: absolute; right: 4px; top: 66px; font-style: normal; font-size: 13px; line-height: 16px; color: var(--brand-blue); }
  .connect { position: absolute; left: 0; top: 279px; width: 292px; }
  .social { position: absolute; left: 81px; top: 322px; display: flex; gap: 6px; }
  .social span { width: 29px; height: 29px; border-radius: 4px; background: #3b3b3b; }

  .btn-more {
    position: absolute; height: 26px; padding: 0 13px; border: 1px solid var(--line); border-radius: 7px;
    background: linear-gradient(#fff, #eef2f5); color: var(--brand-blue);
    font-family: "Source Sans 3", sans-serif; font-weight: 600; font-size: 12.5px; line-height: 24px;
  }

  .footer-nav {
    position: absolute; left: 0; top: 874px; width: 1200px; height: 67px; background: #fbfdfe;
    display: flex; justify-content: center; padding-top: 28px;
    font-family: "Roboto Condensed", sans-serif; font-size: 12.5px; color: #777;
  }
  .footer-nav a { color: inherit; text-decoration: none; white-space: nowrap; }
  .footer-nav a + a::before { content: "|"; margin: 0 10px; color: #aaa; }
  .site-footer {
    position: absolute; left: 0; top: 941px; width: 1200px; height: 43px; background: var(--brand-blue);
    color: #e8f1fa; font-family: "Roboto Condensed", sans-serif; font-size: 11px; text-align: center; line-height: 43px;
  }
</style>
</head>
<body>
  <header class="site-header">
    <div class="brand"><span class="brand-dot"></span>PeopleDeskly</div>
    <nav class="utility-links" aria-label="Quick links">
      <svg viewBox="0 0 24 24" aria-label="Home"><path d="M12 3 1 13h3v8h6v-6h4v6h6v-8h3z"/></svg>
      <svg viewBox="0 0 24 24" aria-label="About"><path d="M4 2h16v16h-5l-3 4-3-4H4zM12 5a3 3 0 1 0 0 6 3 3 0 0 0 0-6zm-5 11h10c0-3-2-4-5-4s-5 1-5 4z"/></svg>
      <svg viewBox="0 0 24 24" aria-label="Contact"><path d="M6 2 9 2 10 8 7.5 9.5C8.5 13 11 15.5 14.5 16.5L16 14l6 1v3c0 2-2 3-3 3C10 20 4 14 3 5c0-1 1-3 3-3z"/></svg>
    </nav>
  </header>

  <nav class="main-nav" aria-label="Main">
    <a class="is-active" href="#" style="left:34px">Attract</a>
    <a href="#" style="left:125px">Recruit</a>
    <a href="#" style="left:208px">Induction</a>
    <a href="#" style="left:309px">Engage</a>
    <a href="#" style="left:394px">Performance</a>
    <a href="#" style="left:512px">Temination &amp; Management</a>
    <a href="#" style="left:717px">Community Redundancy</a>
  </nav>

  <section class="hero">
    <div class="hero-photo" role="img" aria-label="Photo of a smiling businessman in front of a row of colleagues"></div>
    <div class="hero-tab"></div>
    <div class="hero-label">DIY</div>
    <div class="hero-dots"><span></span><span></span><span class="is-current"></span></div>
  </section>

  <div class="column-divider" style="left:450px"></div>
  <div class="column-divider" style="left:755px"></div>

  <section class="column about">
    <h2>About PeopleDeskly</h2>
    <p>Lorem ipsum dolor sit amet, consectetur adipisicing elit, sed do eiusmod tempor incididunt ut labore et dolore magna aliqua. Ut enim ad minim veniam, quis nostrud exercitation ullamco laboris nisi ut aliquip ex ea commodo consequat. Duis aute irure dolor in reprehenderit in voluptate velit esse cillum</p>
    <p>quis nostrud exercitation ullamco laboris nisi ut aliquip ex ea commodo consequat. Duis aute irure dolor in reprehenderit in voluptate velit esse cillum</p>
  </section>
  <a class="btn-more" style="left:357px;top:821px">MORE...</a>

  <section class="column news">
    <h2>News / Community</h2>
    <article class="news-item"><div class="date-badge">Jun<strong>22</strong>2012</div><p>Lorem ipsum dolor sit amet, consectetur adipisicing elit, sed do eiusmod tempor Lorem ipsum</p></article>
    <article class="news-item"><div class="date-badge">Jun<strong>22</strong>2012</div><p>Lorem ipsum dolor sit amet, consectetur adipisicing elit, sed do eiusmod tempor Lorem ipsum</p></article>
    <article class="news-item"><div class="date-badge">Jun<strong>22</strong>2012</div><p>Lorem ipsum dolor sit amet, consectetur adipisicing elit, sed do eiusmod tempor Lorem ipsum</p></article>
  </section>
  <a class="btn-more" style="left:654px;top:815px">MORE...</a>

  <section class="column partners">
    <h2>Our Partners</h2>
    <div class="partner" style="top:46px"><div class="partner-badge"><span></span></div><p>Lorem ipsum dolor sit amet, consectetur tempor Lorem ipsum</p><cite>- Author name</cite></div>
    <div class="partner" style="top:152px"><div class="partner-badge"><span></span></div><p>Lorem ipsum dolor sit amet, consectetur tempor Lorem ipsum</p><cite>- Author name</cite></div>
    <h2 class="connect">Connect with Us</h2>
    <div class="social" aria-label="Social links"><span></span><span></span><span></span><span></span></div>
  </section>
  <a class="btn-more" style="left:955px;top:750px">MORE...</a>

  <nav class="footer-nav" aria-label="Footer">
    <a href="#">Home</a><a href="#">About us</a><a href="#">Attract</a><a href="#">Recruit</a><a href="#">Induction</a><a href="#">Engage</a><a href="#">Performance</a><a href="#">Temination &amp; Management</a><a href="#">Community Redundancy</a><a href="#">Contact us</a>
  </nav>
  <footer class="site-footer">Copyright© 2012. www.peopledeskly.com</footer>
</body>
</html>
```